Marketing Agency Portfolio Brochure

Copper Heron Meridian Holdings is a marketing entity representing diverse brands and services. We are seeking a graphic designer to create a corporate brochure template that showcases the unique offerings of four distinct categories: Equestrian Facility, Freestyle Motocross Team, Aerobatic Team, and Property Portfolio. The brochure should have a sophisticated corporate look and feel, allowing for easy expansion and customization in the future.

Brand Details:

Company Name: Copper Heron Meridian Holdings
Tone: Corporate, Professional, Versatile
Brochure Structure:

Each category will have a four-page spread.
Page 1: Introduction to the specific product or brand.
Pages 2-4: Presentation of offerings, details, and key highlights.
Category Details:

Equestrian Facility:

Introduction: Brief overview of the equestrian facility.
Offering Pages: Showcase services, amenities, and unique features.
Freestyle Motocross Team:

Introduction: Brief overview of the freestyle motocross team.
Offering Pages: Highlight team achievements, members, and upcoming events.
Aerobatic Team:

Introduction: Brief overview of the aerobatic team.
Offering Pages: Showcase team expertise, performances, and services offered.
Property Portfolio:

Introduction: Brief overview of the property portfolio.
Offering Pages: Showcase properties, locations, and key features.
Design Requirements:

Corporate Look and Feel:

Professional and versatile design suitable for a corporate audience.
Consistent color scheme and typography throughout.
Template Flexibility:

Allow for easy customization and expansion for future additions or modifications.
Maintain a cohesive design for each category while allowing for unique elements.
Visual Elements:

Use high-quality images representative of each category.
Incorporate clean and modern layouts.

Sample needs to make provision for all categories, not only one. the brochure needs to have a cover page with the main logo

```html
<!DOCTYPE html>
<html lang="en">
<head>
<meta charset="utf-8">
<title>Copper Heron Meridian Holdings – Corporate Brochure</title>
<link rel="stylesheet" href="https://fonts.googleapis.com/css2?family=Poppins:wght@300;400;500;600;700;800&display=swap">
<style>
:root{
  --backdrop:#b9b9bb;
  --black:#0b0b0d;
  --charcoal:#18181b;
  --ink:#151517;
  --muted:#5c5c62;
  --paper:#f3f3f4;
  --paper-light:#f8f8f9;
  --band:#e3e3e6;
  --white:#ffffff;
  --silver:#c7c9d0;
  --violet-deep:#1f1c36;
  --violet:#453f73;
  --lilac:#9893c0;
}
*{box-sizing:border-box}
html,body{margin:0;padding:0}
body{width:1200px;height:3103px;overflow:hidden;background:var(--backdrop);position:relative;font-family:'Poppins',sans-serif;color:var(--ink)}
.page{position:absolute;overflow:hidden;box-shadow:0 6px 16px rgba(0,0,0,.28)}

/* ---------- Front cover ---------- */
.cover-front{width:466px;height:645px;background:var(--white)}
.cover-front .hero-photo{position:absolute;left:0;top:0;width:466px;height:470px;background:linear-gradient(165deg,#17152b 0%,#2f2b52 35%,#57518a 65%,#8f89b8 100%)}
.cover-front .wedge{position:absolute;left:0;top:0}
.cover-front .headline{position:absolute;left:32px;top:38px;margin:0;font-size:25px;line-height:1.28;font-weight:800;color:var(--white);text-transform:uppercase;letter-spacing:.3px}
.cover-front .brand-list{position:absolute;left:32px;top:156px;margin:0;padding:0;list-style:none;color:#e8e6f4;font-size:13px;font-weight:300;line-height:1.55}
.cover-front .brand-list li::before{content:"• "}
.cover-front .cover-name{position:absolute;right:30px;bottom:30px;width:210px;display:flex;align-items:center;gap:10px}
.brand-square{flex:none;width:12px;height:12px;background:var(--ink)}
.cover-front .cover-name span{font-size:16px;font-weight:600;line-height:1.2;color:var(--ink)}

/* ---------- Back cover ---------- */
.cover-back{width:466px;height:645px;background:radial-gradient(ellipse at 60% 35%,#2a2a2f 0%,#121214 55%,#050506 100%)}
.cover-back .back-name{position:absolute;left:0;right:0;top:72px;text-align:center;font-size:19px;font-weight:600;color:var(--white);letter-spacing:.5px}
.cover-back .contact{position:absolute;left:0;right:0;top:478px;text-align:center;color:var(--white)}
.cover-back .contact h3{margin:0;font-size:18px;font-weight:700;letter-spacing:.3px}
.contact-icons{display:flex;justify-content:center;gap:5px;margin:8px 0 10px}
.contact-icons svg{width:15px;height:15px}
.cover-back .contact p{margin:0;font-size:11.5px;line-height:1.3;font-weight:300}
.cover-back .contact .company{font-weight:500;text-transform:uppercase}

/* ---------- Inner pages ---------- */
.sheet{width:483px;height:696px;background:var(--paper)}
.sheet.light{background:var(--paper-light)}
.page-header{position:absolute;left:0;top:0;width:100%;height:229px;background:var(--charcoal)}
.header-photo{position:absolute;top:0;right:0;height:229px;clip-path:polygon(24% 0,100% 0,100% 86%,93% 100%,0 100%)}
.eyebrow{position:absolute;left:32px;top:38px;font-size:13px;font-weight:400;letter-spacing:3.2px;color:#e6e6e6}
.page-title{position:absolute;left:32px;top:68px;margin:0;font-size:24px;line-height:1.22;color:var(--white);font-weight:300}
.page-title b{font-weight:700}
.lead{position:absolute;font-size:14px;font-weight:600;line-height:1.45;color:var(--ink);margin:0}
.body-text{position:absolute;margin:0;font-size:7.2px;line-height:1.6;color:var(--muted);font-weight:400}
.body-text b{color:var(--ink);font-weight:600}
.chevron{position:absolute;font-size:20px;font-weight:700;color:var(--ink)}
.bracket{position:absolute;border-left:1px solid #9a9aa0;border-top:1px solid #9a9aa0}
.page-footer{position:absolute;left:32px;right:28px;bottom:18px;display:flex;justify-content:space-between;align-items:center}
.page-footer .web{font-size:10px;color:var(--ink)}
.page-footer .web b{font-weight:600}
.page-footer .foot-name{font-size:8px;font-weight:600;color:var(--ink);text-align:right;width:90px;line-height:1.2}

/* motivators band */
.motivators{position:absolute;left:0;top:554px;width:100%;height:73px;background:var(--band)}
.motivators .label{position:absolute;left:0;top:0;width:130px;height:73px;background:var(--black);color:var(--white);font-size:9.5px;font-weight:600;line-height:1.35;padding:14px 0 0 32px}
.motivator{position:absolute;top:18px;width:100px;display:flex;gap:6px}
.motivator h4{margin:0;font-size:7.5px;font-weight:700}
.motivator p{margin:1px 0 0;font-size:5.6px;line-height:1.45;color:var(--muted)}
.icon-dot{flex:none;width:22px;height:22px;border-radius:50%;background:var(--black);display:flex;align-items:center;justify-content:center}
.icon-dot svg{width:12px;height:12px}

/* services diagram */
.diagram-core{position:absolute;left:186px;top:415px;width:110px;height:110px;background:var(--black);transform:rotate(45deg);border-radius:8px}
.diagram-name{position:absolute;left:186px;top:452px;width:110px;text-align:center;color:var(--white);font-size:10px;font-weight:600;line-height:1.25}
.service-node{position:absolute;width:30px;height:30px;border-radius:50%;background:var(--black);border:2px solid var(--white);box-shadow:0 0 0 1px var(--black);display:flex;align-items:center;justify-content:center}
.service-node svg{width:15px;height:15px}
.service{position:absolute;width:128px}
.service h4{margin:0;font-size:7.5px;font-weight:700}
.service p{margin:2px 0 0;font-size:5.4px;line-height:1.45;color:var(--muted)}
.service.left{text-align:right}

/* amenities */
.offer-bar{position:absolute;left:0;top:0;width:100%;height:59px}
.section-title{position:absolute;left:32px;margin:0;font-size:22px;font-weight:700;color:var(--ink)}
.section-title::before{content:"› ";}
.amenity{position:absolute;width:136px}
.amenity .photo{width:136px;height:94px}
.amenity span{display:block;text-align:center;margin-top:10px;font-size:8px;font-weight:600}
.feature{position:absolute;width:200px;display:flex;gap:14px}
.feature .diamond{flex:none;width:36px;height:36px;margin:6px 0 0 6px;background:var(--black);transform:rotate(45deg);border-radius:4px;display:flex;align-items:center;justify-content:center}
.feature .diamond svg{width:18px;height:18px;transform:rotate(-45deg)}
.feature h4{margin:0;font-size:8.5px;font-weight:600}
.feature p{margin:1px 0 0;font-size:7px;line-height:1.45;color:var(--muted);text-align:justify}

/* highlights */
.highlight{position:absolute;left:32px;width:425px}
.highlight .bracket{left:0;top:0;width:20px;height:78px}
.highlight h3{margin:0 0 0 42px;font-size:15px;font-weight:600;color:var(--ink)}
.highlight p{margin:8px 0 0 42px;font-size:7.2px;line-height:1.6;color:var(--muted)}
</style>
</head>
<body>

<!-- ================= Outside spread (back + front, flat) ================= -->
<section class="page cover-back" style="left:134px;top:135px">
  <div class="back-name">Copper Heron Meridian Holdings</div>
  <div class="contact">
    <h3>GET IN TOUCH</h3>
    <div class="contact-icons">
      <svg viewBox="0 0 16 16"><circle cx="8" cy="8" r="8" fill="#fff"/><path d="M8 3.5a2.8 2.8 0 0 0-2.8 2.8C5.2 8.5 8 12 8 12s2.8-3.5 2.8-5.7A2.8 2.8 0 0 0 8 3.5z" fill="#000"/><circle cx="8" cy="6.3" r="1" fill="#fff"/></svg>
      <svg viewBox="0 0 16 16"><circle cx="8" cy="8" r="8" fill="#fff"/><path d="M5 4l2 .3.6 2-1.2.8a6 6 0 0 0 2.5 2.5l.8-1.2 2 .6.3 2-1.3.8C7.6 11.8 4.2 8.4 4.2 5.3z" fill="#000"/></svg>
      <svg viewBox="0 0 16 16"><circle cx="8" cy="8" r="8" fill="#fff"/><circle cx="8" cy="8" r="4" fill="none" stroke="#000" stroke-width="1"/><path d="M4 8h8M8 4c-2 2.5-2 5.5 0 8M8 4c2 2.5 2 5.5 0 8" fill="none" stroke="#000" stroke-width=".8"/></svg>
      <svg viewBox="0 0 16 16"><circle cx="8" cy="8" r="8" fill="#fff"/><rect x="4" y="5.2" width="8" height="5.6" rx=".6" fill="#000"/><path d="M4.3 5.6L8 8.4l3.7-2.8" fill="none" stroke="#fff" stroke-width=".8"/></svg>
    </div>
    <p class="company">Copper Heron Meridian Holdings</p>
    <p>88 Harbour Lorem Drive, Suite 40</p>
    <p>Lakeport, CA 90000</p>
    <p>(555) 010-2040 &nbsp;|&nbsp; (555) 010-2041</p>
    <p>info@copperheronmeridian.example</p>
  </div>
</section>

<section class="page cover-front" style="left:600px;top:135px">
  <div class="hero-photo" role="img" aria-label="Businessman in a lilac blazer holding a tablet, looking upward against a dark city backdrop"></div>
  <svg class="wedge" width="466" height="645" viewBox="0 0 466 645"><polygon points="0,420 466,300 466,318 0,438" fill="#c7c9d0"/><polygon points="0,446 466,326 466,645 0,645" fill="#fff"/></svg>
  <h1 class="headline">Diverse brands<br>and corporate<br>services</h1>
  <ul class="brand-list"><li>Equestrian Facility</li><li>Freestyle Motocross Team</li><li>Aerobatic Team</li><li>Property Portfolio</li></ul>
  <div class="cover-name"><span class="brand-square"></span><span>Copper Heron Meridian Holdings</span></div>
</section>

<!-- ================= Front and back covers ================= -->
<section class="page cover-front" style="left:111px;top:858px">
  <div class="hero-photo" role="img" aria-label="Businessman in a lilac blazer holding a tablet, looking upward against a dark city backdrop"></div>
  <svg class="wedge" width="466" height="645" viewBox="0 0 466 645"><polygon points="0,420 466,300 466,318 0,438" fill="#c7c9d0"/><polygon points="0,446 466,326 466,645 0,645" fill="#fff"/></svg>
  <h1 class="headline">Diverse brands<br>and corporate<br>services</h1>
  <ul class="brand-list"><li>Equestrian Facility</li><li>Freestyle Motocross Team</li><li>Aerobatic Team</li><li>Property Portfolio</li></ul>
  <div class="cover-name"><span class="brand-square"></span><span>Copper Heron Meridian Holdings</span></div>
</section>

<section class="page cover-back" style="left:615px;top:858px">
  <div class="back-name">Copper Heron Meridian Holdings</div>
  <div class="contact">
    <h3>GET IN TOUCH</h3>
    <div class="contact-icons">
      <svg viewBox="0 0 16 16"><circle cx="8" cy="8" r="8" fill="#fff"/><path d="M8 3.5a2.8 2.8 0 0 0-2.8 2.8C5.2 8.5 8 12 8 12s2.8-3.5 2.8-5.7A2.8 2.8 0 0 0 8 3.5z" fill="#000"/><circle cx="8" cy="6.3" r="1" fill="#fff"/></svg>
      <svg viewBox="0 0 16 16"><circle cx="8" cy="8" r="8" fill="#fff"/><path d="M5 4l2 .3.6 2-1.2.8a6 6 0 0 0 2.5 2.5l.8-1.2 2 .6.3 2-1.3.8C7.6 11.8 4.2 8.4 4.2 5.3z" fill="#000"/></svg>
      <svg viewBox="0 0 16 16"><circle cx="8" cy="8" r="8" fill="#fff"/><circle cx="8" cy="8" r="4" fill="none" stroke="#000" stroke-width="1"/><path d="M4 8h8M8 4c-2 2.5-2 5.5 0 8M8 4c2 2.5 2 5.5 0 8" fill="none" stroke="#000" stroke-width=".8"/></svg>
      <svg viewBox="0 0 16 16"><circle cx="8" cy="8" r="8" fill="#fff"/><rect x="4" y="5.2" width="8" height="5.6" rx=".6" fill="#000"/><path d="M4.3 5.6L8 8.4l3.7-2.8" fill="none" stroke="#fff" stroke-width=".8"/></svg>
    </div>
    <p class="company">Copper Heron Meridian Holdings</p>
    <p>88 Harbour Lorem Drive, Suite 40</p>
    <p>Lakeport, CA 90000</p>
    <p>(555) 010-2040 &nbsp;|&nbsp; (555) 010-2041</p>
    <p>info@copperheronmeridian.example</p>
  </div>
</section>

<!-- ================= Spread: pages 01–02 ================= -->
<section class="page sheet" style="left:114px;top:1557px">
  <header class="page-header">
    <div class="header-photo" role="img" aria-label="Smiling businesswoman working on a laptop in a bright office" style="left:190px;width:293px;background:linear-gradient(135deg,#a98a63 0%,#d9c6a8 45%,#f1ebe2 70%,#c9b08c 100%)"></div>
    <div class="eyebrow">Introduction</div>
    <h2 class="page-title">Brief<br>overview of the<br><b>Equestrian<br>Facility</b></h2>
  </header>
  <div class="chevron" style="left:32px;top:262px">›</div>
  <div class="bracket" style="left:34px;top:292px;width:18px;height:130px;border-top:none"></div>
  <p class="lead" style="left:84px;top:266px;width:370px">Lorem Ipsum is simply dummy text of the printing and typesetting industry. Lorem Ipsum.</p>
  <p class="body-text" style="left:84px;top:318px;width:370px"><b>Set on open acreage,</b> the facility offers modern stabling, covered arenas and trail access, supported by a team that keeps every horse fit, calm and well cared for.</p>
  <p class="body-text" style="left:84px;top:364px;width:170px">Daily routines are built around each horse, with tailored feeding, turnout and exercise plans. Qualified grooms and visiting vets work side by side, while riders enjoy clean tack rooms, wash bays and secure parking for floats. Coaching is available for beginners through to competitors preparing for regional shows and clinics.</p>
  <p class="body-text" style="left:280px;top:364px;width:170px">Events run through the year, from dressage days to jumping series and pony club rallies. The grounds host private lessons, agistment and short stays for visiting horses, and every booking is handled by one friendly office team that knows the property, the horses and the people well.</p>
  <p class="body-text" style="left:32px;top:508px;width:422px"><b>Whether you ride</b> for pleasure or compete, we provide the space, care and guidance to help you and your horse progress with confidence.</p>
  <div class="motivators">
    <div class="label">The Key<br>motivators for<br>any team are</div>
    <div class="motivator" style="left:140px"><span class="icon-dot"><svg viewBox="0 0 12 12"><path d="M6 1l1.5 3 3.3.4-2.4 2.3.6 3.3L6 8.4 3 10l.6-3.3L1.2 4.4 4.5 4z" fill="#fff"/></svg></span><div><h4>QUALITY</h4><p>High standards in every detail.</p></div></div>
    <div class="motivator" style="left:250px"><span class="icon-dot"><svg viewBox="0 0 12 12"><path d="M6 1L10 2.5V6c0 2.5-2 4.2-4 5-2-.8-4-2.5-4-5V2.5z" fill="#fff"/></svg></span><div><h4>INTEGRITY</h4><p>Honest, open and fair dealings.</p></div></div>
    <div class="motivator" style="left:360px"><span class="icon-dot"><svg viewBox="0 0 12 12"><path d="M2 6.5l2.5 2.5L10 3.5" fill="none" stroke="#fff" stroke-width="1.8"/></svg></span><div><h4>TRUST</h4><p>Relationships built to last.</p></div></div>
  </div>
  <footer class="page-footer"><span class="web">www.<b>copperheronmeridian</b>.example &nbsp;|&nbsp; 01</span><span class="foot-name">Copper Heron Meridian Holdings</span></footer>
</section>

<section class="page sheet light" style="left:597px;top:1557px">
  <header class="page-header">
    <div class="header-photo" role="img" aria-label="Two colleagues reviewing a tablet together in a modern office" style="left:150px;width:333px;background:linear-gradient(135deg,#3b3f4a 0%,#8a8f99 40%,#c9c3ba 65%,#6f3b3b 100%)"></div>
    <div class="eyebrow">Offering</div>
    <h2 class="page-title">Showcase<br><b>Company<br>services</b></h2>
  </header>
  <p class="lead" style="left:40px;top:268px;width:403px;text-align:center">Lorem Ipsum is simply dummy text of the printing and typesetting industry. Lorem Ipsum.</p>
  <p class="body-text" style="left:32px;top:322px;width:420px"><b>We bring together</b> specialist services under one trusted name, so clients deal with a single team from first enquiry to final delivery, with clear pricing throughout.</p>
  <div class="diagram-core"></div>
  <div class="diagram-name">Copper Heron Meridian Holdings</div>

  <div class="service-node" style="left:182px;top:398px"><svg viewBox="0 0 16 16"><path d="M8 2l1.8 3.6 4 .6-2.9 2.8.7 4L8 11.1 4.4 13l.7-4L2.2 6.2l4-.6z" fill="#fff"/></svg></div>
  <div class="service-node" style="left:272px;top:398px"><svg viewBox="0 0 16 16"><path d="M3 13V8h2v5zM7 13V5h2v8zM11 13V3h2v10z" fill="#fff"/></svg></div>
  <div class="service-node" style="left:150px;top:455px"><svg viewBox="0 0 16 16"><circle cx="8" cy="8" r="5" fill="none" stroke="#fff" stroke-width="1.6"/><circle cx="8" cy="8" r="1.8" fill="#fff"/></svg></div>
  <div class="service-node" style="left:304px;top:455px"><svg viewBox="0 0 16 16"><path d="M3 8h8M8 4.5L11.5 8 8 11.5" fill="none" stroke="#fff" stroke-width="1.8"/></svg></div>
  <div class="service-node" style="left:182px;top:512px"><svg viewBox="0 0 16 16"><path d="M3.5 8.5l3 3 6-6.5" fill="none" stroke="#fff" stroke-width="1.8"/></svg></div>
  <div class="service-node" style="left:272px;top:512px"><svg viewBox="0 0 16 16"><path d="M2 13V9h3v4zM6.5 13V6h3v7zM11 13V3h3v10z" fill="#fff"/></svg></div>

  <div class="service left" style="left:40px;top:396px"><h4>SERVICE ONE</h4><p>A brief line that explains this service and its core benefit.</p></div>
  <div class="service left" style="left:14px;top:455px"><h4>SERVICE TWO</h4><p>A brief line that explains this service and who it serves.</p></div>
  <div class="service left" style="left:40px;top:514px"><h4>SERVICE THREE</h4><p>A brief line that explains this service and how it works.</p></div>
  <div class="service" style="left:315px;top:396px"><h4>SERVICE FOUR</h4><p>A brief line that explains this service and its key result.</p></div>
  <div class="service" style="left:345px;top:455px"><h4>SERVICE FIVE</h4><p>A brief line that explains this service and its main value.</p></div>
  <div class="service" style="left:315px;top:514px"><h4>SERVICE SIX</h4><p>A brief line that explains this service and why it matters.</p></div>

  <p class="body-text" style="left:32px;top:592px;width:420px"><b>Every service</b> can be booked on its own or combined into a package, and our coordinators will tailor the plan to your goals and timeline.</p>
  <footer class="page-footer"><span class="web">www.<b>copperheronmeridian</b>.example &nbsp;|&nbsp; 02</span><span class="foot-name">Copper Heron Meridian Holdings</span></footer>
</section>

<!-- ================= Spread: pages 03–04 ================= -->
<section class="page sheet" style="left:117px;top:2305px">
  <svg class="offer-bar" width="483" height="59" viewBox="0 0 483 59"><polygon points="0,0 483,0 483,8 405,59 0,59" fill="#0b0b0d"/></svg>
  <div class="eyebrow" style="top:22px">Offering</div>
  <h2 class="section-title" style="top:80px">Amenities</h2>
  <div class="amenity" style="left:32px;top:129px"><div class="photo" role="img" aria-label="Team stacking hands together over a table" style="background:linear-gradient(135deg,#5a4e48,#a9978a,#3b3a44)"></div><span>Amenities 1</span></div>
  <div class="amenity" style="left:172px;top:129px"><div class="photo" role="img" aria-label="Colleagues discussing work in an office" style="background:linear-gradient(135deg,#8b8f97,#d6d1c9,#6c4a48)"></div><span>Amenities 2</span></div>
  <div class="amenity" style="left:312px;top:129px"><div class="photo" role="img" aria-label="Businessman with a tablet in violet light" style="background:linear-gradient(135deg,#2b2850,#5d578e,#9c97c2)"></div><span>Amenities 3</span></div>
  <div class="amenity" style="left:32px;top:268px"><div class="photo" role="img" aria-label="Modern glass office buildings against the sky" style="background:linear-gradient(160deg,#1d3a66,#4d74a8,#b9cbe0)"></div><span>Amenities 4</span></div>
  <div class="amenity" style="left:172px;top:268px"><div class="photo" role="img" aria-label="Woman working on a laptop in a warm office" style="background:linear-gradient(135deg,#a98a63,#e3d4bd,#b89a74)"></div><span>Amenities 5</span></div>
  <div class="amenity" style="left:312px;top:268px"><div class="photo" role="img" aria-label="Business people in a bright meeting room" style="background:linear-gradient(135deg,#cfd6dc,#8d9aa6,#e9ecef)"></div><span>Amenities 6</span></div>

  <h2 class="section-title" style="top:415px">Unique Features</h2>
  <div class="feature" style="left:32px;top:488px"><span class="diamond"><svg viewBox="0 0 18 18"><circle cx="9" cy="9" r="5.5" fill="none" stroke="#fff" stroke-width="1.6"/><path d="M9 6v3.3l2.2 1.4" fill="none" stroke="#fff" stroke-width="1.5"/></svg></span><div><h4>Features One</h4><p>Short description of this feature and the value it brings to members and guests.</p></div></div>
  <div class="feature" style="left:248px;top:488px"><span class="diamond"><svg viewBox="0 0 18 18"><rect x="3" y="6" width="12" height="8" rx="1" fill="#fff"/><path d="M7 6V4.5h4V6" fill="none" stroke="#fff" stroke-width="1.4"/></svg></span><div><h4>Features Three</h4><p>Short description of this feature and the value it brings to members and guests.</p></div></div>
  <div class="feature" style="left:32px;top:562px"><span class="diamond"><svg viewBox="0 0 18 18"><path d="M4 12l7-7 2 2-7 7H4z" fill="#fff"/></svg></span><div><h4>Features Two</h4><p>Short description of this feature and the value it brings to members and guests.</p></div></div>
  <div class="feature" style="left:248px;top:562px"><span class="diamond"><svg viewBox="0 0 18 18"><circle cx="9" cy="9" r="3" fill="#fff"/><path d="M9 2v3M9 13v3M2 9h3M13 9h3M4 4l2 2M12 12l2 2M14 4l-2 2M6 12l-2 2" stroke="#fff" stroke-width="1.6"/></svg></span><div><h4>Features Four</h4><p>Short description of this feature and the value it brings to members and guests.</p></div></div>
  <footer class="page-footer"><span class="web">www.<b>copperheronmeridian</b>.example &nbsp;|&nbsp; 03</span><span class="foot-name">Copper Heron Meridian Holdings</span></footer>
</section>

<section class="page sheet light" style="left:600px;top:2305px">
  <header class="page-header" style="height:225px">
    <div class="header-photo" role="img" aria-label="Two smiling business colleagues working at a laptop" style="left:170px;width:313px;height:225px;background:linear-gradient(135deg,#4c5058 0%,#b8bcc2 40%,#e8e4dc 65%,#8d7f70 100%)"></div>
    <div class="eyebrow">Introduction</div>
    <h2 class="page-title"><b>Key<br>Highlights</b></h2>
  </header>
  <div class="highlight" style="top:267px"><div class="bracket"></div><h3>KEY HIGHLIGHTS ONE</h3><p>A short summary of this highlight goes here, describing what makes it stand out, the results it has delivered and why clients return. Replace this text with facts, figures or a brief story that supports the category being presented.</p></div>
  <div class="highlight" style="top:361px"><div class="bracket"></div><h3>KEY HIGHLIGHTS TWO</h3><p>A short summary of this highlight goes here, describing what makes it stand out, the results it has delivered and why clients return. Replace this text with facts, figures or a brief story that supports the category being presented.</p></div>
  <div class="highlight" style="top:456px"><div class="bracket"></div><h3>KEY HIGHLIGHTS THREE</h3><p>A short summary of this highlight goes here, describing what makes it stand out, the results it has delivered and why clients return. Replace this text with facts, figures or a brief story that supports the category being presented.</p></div>
  <div class="highlight" style="top:556px"><div class="bracket"></div><h3>KEY HIGHLIGHTS FOUR</h3><p>A short summary of this highlight goes here, describing what makes it stand out, the results it has delivered and why clients return. Replace this text with facts, figures or a brief story that supports the category being presented.</p></div>
  <footer class="page-footer"><span class="web">www.<b>copperheronmeridian</b>.example &nbsp;|&nbsp; 04</span><span class="foot-name">Copper Heron Meridian Holdings</span></footer>
</section>

</body>
</html>
```